Business Cards for Internet Security Company

Awesome designers! This is the opportunity to help design cards for a forward thinking network security company. They use threat information gathered from peer groups to make intelligent decisions on what threats are relevant and which arent. ( not that you need this to do designs, but just so you know where they are coming from. ) :-)

We'd like to see a two side design and the deliverables will be in illustrator 4. The logo is attached and the logo colors are attached in the JPG and I've attached a an eps of the logo and icon

Security

```html
<!DOCTYPE html>
<html lang="en">
<head>
<meta charset="utf-8">
<title>Quorlane Business Cards</title>
<link rel="stylesheet" href="https://fonts.googleapis.com/css2?family=Didact+Gothic&family=Montserrat:wght@300;400;600&display=swap">
<style>
  :root {
    --page-bg: #e9e6e1;
    --card-light: #8cc4f2;
    --card-mid: #3f79b8;
    --card-dark: #1c3f6e;
    --card-deep: #142f55;
    --ink: #ffffff;
    --ink-soft: rgba(255,255,255,0.82);
    --name-accent: #9fd0ff;
    --rule: rgba(255,255,255,0.55);
  }
  * { box-sizing: border-box; margin: 0; padding: 0; }
  html, body { width: 1200px; height: 1000px; overflow: hidden; }
  body {
    background: var(--page-bg);
    font-family: "Montserrat", Arial, sans-serif;
    display: flex;
    flex-direction: column;
    align-items: center;
    justify-content: center;
    gap: 70px;
  }
  .card {
    position: relative;
    width: 560px;
    height: 320px;
    border-radius: 22px;
    overflow: hidden;
    color: var(--ink);
    background:
      radial-gradient(ellipse 70% 90% at 0% 30%, var(--card-light) 0%, rgba(140,196,242,0) 70%),
      linear-gradient(100deg, var(--card-mid) 0%, var(--card-dark) 55%, var(--card-deep) 100%);
    box-shadow: 0 10px 24px rgba(20,40,70,0.25);
  }
  .card::after {
    content: "";
    position: absolute;
    left: -10%; right: -10%; top: 62%;
    height: 60px;
    background: linear-gradient(180deg, rgba(255,255,255,0) 0%, rgba(255,255,255,0.07) 50%, rgba(255,255,255,0) 100%);
    transform: rotate(-4deg);
  }

  /* Front */
  .card-front .brand {
    position: absolute;
    left: 0; right: 0; top: 100px;
    text-align: center;
  }
  .brand-line {
    display: inline-flex;
    align-items: center;
    gap: 14px;
  }
  .brand-dot {
    width: 46px; height: 46px;
    border: 7px solid var(--ink);
    border-radius: 50%;
  }
  .brand-name {
    font-family: "Didact Gothic", Arial, sans-serif;
    font-size: 76px;
    line-height: 1;
    color: var(--ink);
  }
  .tagline {
    margin-top: 14px;
    font-size: 15px;
    font-weight: 300;
    letter-spacing: 0.42em;
    text-transform: uppercase;
    color: var(--ink-soft);
  }

  /* Back */
  .card-back .mark {
    position: absolute;
    left: 36px; bottom: 40px;
    width: 224px;
    display: flex;
    align-items: center;
    gap: 12px;
    z-index: 1;
  }
  .mark-ring {
    flex: none;
    width: 100px; height: 100px;
    border: 18px solid var(--ink);
    border-radius: 50%;
  }
  .mark-name {
    font-family: "Didact Gothic", Arial, sans-serif;
    font-size: 26px;
    line-height: 1;
    white-space: nowrap;
    color: var(--ink);
  }
  .contact-block {
    position: absolute;
    right: 34px; top: 34px;
    width: 250px;
    z-index: 1;
  }
  .person-name {
    font-size: 34px;
    font-weight: 400;
    line-height: 0.95;
    text-transform: uppercase;
    color: var(--name-accent);
  }
  .person-name .first { font-weight: 300; display: block; }
  .person-name .last { font-weight: 600; display: block; }
  .person-role {
    margin-top: 6px;
    font-size: 11px;
    font-weight: 300;
    line-height: 1.4;
    color: var(--ink-soft);
  }
  .contact-rule {
    height: 1px;
    background: var(--rule);
    margin: 12px 0 12px -16px;
  }
  .contact-list { list-style: none; }
  .contact-list li {
    display: flex;
    align-items: flex-start;
    gap: 9px;
    font-size: 11px;
    font-weight: 300;
    line-height: 1.45;
    color: var(--ink-soft);
    margin-bottom: 5px;
  }
  .contact-list svg { flex: none; width: 11px; height: 11px; margin-top: 2px; fill: var(--ink); }
</style>
</head>
<body>

<section class="card card-front">
  <div class="brand">
    <div class="brand-line">
      <span class="brand-dot"></span>
      <span class="brand-name">Quorlane</span>
    </div>
    <p class="tagline">Coordinated Cyber Defense</p>
  </div>
</section>

<section class="card card-back">
  <div class="mark">
    <span class="mark-ring"></span>
    <span class="mark-name">Quorlane</span>
  </div>

  <div class="contact-block">
    <h1 class="person-name"><span class="first">Mark</span><span class="last">Odell</span></h1>
    <p class="person-role">Chief Executive Officer<br>&amp; Co-Founder</p>
    <div class="contact-rule"></div>
    <ul class="contact-list">
      <li>
        <svg viewBox="0 0 12 12" aria-hidden="true"><path d="M6 0a4 4 0 0 0-4 4c0 3 4 8 4 8s4-5 4-8a4 4 0 0 0-4-4zm0 5.5A1.5 1.5 0 1 1 6 2.5a1.5 1.5 0 0 1 0 3z"/></svg>
        <span>P.O. Box 2210-00400<br>Central Post, Lakeview</span>
      </li>
      <li>
        <svg viewBox="0 0 12 12" aria-hidden="true"><path d="M2.5 0.5l2 2-1 1.5c.8 1.6 2 2.8 3.5 3.5l1.5-1 2 2-1.5 2C5 10 2 7 0.5 2z"/></svg>
        <span>410 55 20 37<br>720 18 64 93</span>
      </li>
      <li>
        <svg viewBox="0 0 12 12" aria-hidden="true"><path d="M0 2h12v8H0zm1 1v.4l5 3 5-3V3zm0 1.6V9h10V4.6L6 7.6z"/></svg>
        <span>tim@quorlane.com</span>
      </li>
      <li>
        <svg viewBox="0 0 12 12" aria-hidden="true"><circle cx="6" cy="6" r="5.5"/></svg>
        <span>www.quorlane.com</span>
      </li>
    </ul>
  </div>
</section>

</body>
</html>
```